Zertifikat-Design und Garantieschein-Design für Uhrenmanufaktur gesucht
Zielgruppe
Wir sind eine Uhrenmanufaktur und fertigen hochwertige mechanische Armbanduhren in größten Teilen in Handarbeit.
Für die Auslieferung unserer Uhren brauchen wir ein Zertifikat und einen Garantieschein (jeweils 1 Blatt).
Unsere Zielgruppe sind gutverdienende Menschen zwischen 25 und 55 Jahren.
Aufgabenstellung
Es soll jeweils ein Zertifikat erstellt werden (1 Blatt - nur Vorderseite) und ein Garantieschein (1 Blatt - Vorder- und Rückseite). Alle Vorgaben, sowie Bilder der Uhren als Inspiration sind in der PDF enthalten.

```html
<!DOCTYPE html>
<html lang="de">
<head>
<meta charset="utf-8">
<title>Zertifikat – KALDEN</title>
<link href="https://fonts.googleapis.com/css2?family=Roboto+Condensed:wght@300;400;700&family=Great+Vibes&display=swap" rel="stylesheet">
<style>
  :root {
    --ink: #111111;
    --rule-light: #c9c9c9;
    --rule-dark: #222222;
    --paper: #ffffff;
  }
  * { margin: 0; padding: 0; box-sizing: border-box; }
  html, body { width: 845px; height: 1200px; overflow: hidden; background: var(--paper); }
  body { position: relative; font-family: "Roboto Condensed", "Arial Narrow", sans-serif; color: var(--ink); }

  .brand { position: absolute; top: 66px; left: 0; width: 845px; text-align: center; font-weight: 300; font-size: 36px; letter-spacing: 8px; line-height: 1; color: var(--ink); }

  .title { position: absolute; top: 170px; left: 0; width: 845px; text-align: center; font-family: "Great Vibes", cursive; font-size: 72px; font-weight: 400; }

  .field { position: absolute; left: 96px; width: 649px; display: flex; align-items: flex-end; }
  .field .label { white-space: nowrap; padding-right: 18px; }
  .field .line { flex: 1; border-bottom: 1px solid var(--rule-light); margin-bottom: 4px; }

  .spec .label { font-weight: 700; font-size: 18px; }

  .divider { position: absolute; left: 51px; width: 743px; border-top: 1.5px solid var(--rule-dark); }

  .origin { position: absolute; top: 448px; left: 0; width: 845px; text-align: center; font-weight: 300; font-size: 18.5px; line-height: 27px; }

  .components { left: 166px; width: 510px; }
  .components .label { font-weight: 300; font-size: 18px; }

  .party-label { position: absolute; left: 96px; font-weight: 300; font-size: 18px; }
  .party-line { position: absolute; left: 96px; width: 649px; border-top: 1px solid var(--rule-light); }

  .footer { position: absolute; top: 1055px; font-weight: 700; font-size: 18px; }
  .footer.date { left: 96px; }
  .footer.sign { right: 96px; }
</style>
</head>
<body>
  <header class="brand">KALDEN</header>

  <h1 class="title">Zertifikat/Certificate</h1>

  <div class="field spec" style="top:310px"><span class="label">MODELLNAME / MODEL NAME:</span><span class="line"></span></div>
  <div class="field spec" style="top:343px"><span class="label">REFERENZNUMMER / REFERENCE NO.:</span><span class="line"></span></div>
  <div class="field spec" style="top:383px"><span class="label">KALIBER / CALIBER:</span><span class="line"></span></div>

  <div class="divider" style="top:436px"></div>
  <p class="origin">Diese Uhr wurde hergestellt, montiert und einreguliert im KALDEN-Atelier in Dresden.<br>This watch was made, assembled and adjusted in the KALDEN-atelier in Dresden/Germany.</p>
  <div class="divider" style="top:517px"></div>

  <div class="field components" style="top:541px"><span class="label">Gehäuse / Case:</span><span class="line"></span></div>
  <div class="field components" style="top:572px"><span class="label">Glas / Glass:</span><span class="line"></span></div>
  <div class="field components" style="top:603px"><span class="label">Band / Strap:</span><span class="line"></span></div>
  <div class="field components" style="top:633px"><span class="label">Schließe / Buckle:</span><span class="line"></span></div>
  <div class="field components" style="top:664px"><span class="label">Zeiger / Hands:</span><span class="line"></span></div>
  <div class="field components" style="top:694px"><span class="label">Zifferblatt / Dial:</span><span class="line"></span></div>

  <p class="party-label" style="top:752px">Name und Adresse des Käufers / Name and address of purchaser:</p>
  <div class="party-line" style="top:806px"></div>
  <p class="party-label" style="top:816px">Postleitzahl, Stadt und Land / Postal code, City and Land:</p>
  <div class="party-line" style="top:869px"></div>
  <p class="party-label" style="top:874px">Name und Adresse des Verkäufers / Name and address of seller:</p>
  <div class="party-line" style="top:930px"></div>
  <p class="party-label" style="top:936px">Postleitzahl, Stadt und Land / Postal code, &nbsp;City and Land:</p>
  <div class="party-line" style="top:992px"></div>

  <p class="footer date">Ausstellungsdatum / Date of issue</p>
  <p class="footer sign">Unterschrift / Sign</p>
</body>
</html>
```